Velmora - New coded website

Current website is around 5 years old and corrupted in some ways...
I would like to refresh the design and to create a new coded website based on the current content .
Please refer to :
www.velmora-sample.com.au

Coded - Design and coding required

```html
<!DOCTYPE html>
<html lang="en">
<head>
<meta charset="utf-8">
<title>Velmora – Odours Controlled Naturally</title>
<link href="https://fonts.googleapis.com/css2?family=Poppins:wght@400;500;600;700&display=swap" rel="stylesheet">
<style>
:root{
  --green:#6cb33f;
  --green-dark:#4f9a2a;
  --green-soft:#e8f4de;
  --navy:#0e2a3b;
  --ink:#13212d;
  --text:#55606a;
  --muted:#9aa1a8;
  --white:#ffffff;
}
*{box-sizing:border-box;margin:0;padding:0}
html,body{width:1200px;height:4505px;overflow:hidden}
body{font-family:"Poppins",sans-serif;color:var(--ink);background:var(--white);position:relative}
.abs{position:absolute}
a{color:inherit;text-decoration:none}
.btn{position:absolute;display:flex;align-items:center;justify-content:center;background:var(--green);color:var(--white);font-weight:600;font-size:13px;border-radius:24px;letter-spacing:.2px}
.photo{position:absolute}

/* header */
.topbar{left:770px;top:0;width:430px;height:32px;background:var(--green);border-bottom-left-radius:24px;color:var(--white);font-size:10.5px;font-weight:600;display:flex;align-items:center;gap:28px;padding-left:70px}
.topbar span{display:flex;align-items:center;gap:6px}
.brand{left:88px;top:12px;display:flex;align-items:center;gap:10px}
.brand-dot{width:62px;height:62px;border-radius:50%;background:var(--green)}
.brand-name{font-size:32px;font-weight:500;color:var(--navy);line-height:1}
.brand-tag{font-size:10px;color:var(--text);font-style:normal}
.nav{left:392px;top:43px;display:flex;gap:16px;font-size:12px;font-weight:500;color:var(--ink)}

/* hero */
.hero-title{left:88px;top:225px;font-size:55px;font-weight:600;line-height:64px;color:var(--navy)}
.hero-sub{left:88px;top:434px;font-size:13.5px;color:var(--text)}
.hero-photo-big{left:650px;top:79px;width:612px;height:612px;border-radius:50%;background:linear-gradient(160deg,#cfe3f3 0%,#9dbfa6 40%,#5f8a4d 70%,#4d6f3d 100%)}
.hero-photo-small{left:524px;top:433px;width:246px;height:246px;border-radius:50%;border:6px solid var(--white);background:linear-gradient(150deg,#b7d58f 0%,#79a94c 50%,#3f6f2a 100%);box-shadow:0 6px 18px rgba(0,0,0,.12)}

/* section headings */
.h2{position:absolute;left:0;width:1200px;text-align:center;font-size:40px;font-weight:600;color:var(--navy)}

/* feature cards */
.feature{position:absolute;top:845px;width:240px;height:297px;background:var(--white);border-radius:12px;box-shadow:0 8px 30px rgba(0,0,0,.08);text-align:center}
.feature svg{position:absolute;left:80px;top:28px}
.feature h3{position:absolute;top:134px;width:100%;font-size:17px;font-weight:600}
.feature p{position:absolute;top:172px;left:28px;right:28px;font-size:12.5px;line-height:20px;color:var(--text)}
.feature hr{position:absolute;top:250px;left:24px;right:24px;border:0;border-top:1px solid #e7e9ec}
.feature .more{position:absolute;top:265px;width:100%;font-size:10.5px;font-weight:600;color:var(--muted)}

/* about */
.about-bg{left:0;top:1500px}
.about-photo{left:153px;top:1238px;width:456px;height:456px;border-radius:50%;background:linear-gradient(150deg,#d9e79a 0%,#8dbb4c 45%,#4f7f2b 100%)}
.about-title{left:660px;top:1295px;font-size:40px;font-weight:600;color:var(--navy)}
.about-sub{left:660px;top:1352px;font-size:17px;font-weight:500}
.about-text{left:660px;top:1386px;width:390px;font-size:13.5px;line-height:20.5px;color:var(--text)}

/* projects */
.project{position:absolute;top:1849px;width:244px;height:365px;background:var(--white);border-radius:8px;box-shadow:0 8px 26px rgba(0,0,0,.1);overflow:hidden}
.project .pic{height:206px;background:linear-gradient(180deg,#b9c8d6 0%,#8fa596 55%,#6f8373 100%)}
.project .body{position:absolute;top:206px;left:0;right:0;bottom:0;padding:18px 22px 0 24px;border-left:4px solid var(--green);margin-top:14px;height:32px}
.project h4{position:absolute;top:222px;left:24px;font-size:15px;font-weight:500}
.project p{position:absolute;top:254px;left:24px;right:18px;font-size:11.5px;line-height:17.5px;color:var(--text)}
.project .more{position:absolute;top:320px;left:24px;font-size:10.5px;font-weight:600;text-decoration:underline}

/* best */
.best-title{left:212px;top:2357px;font-size:40px;font-weight:600;line-height:49px;color:var(--navy)}
.best-list{left:212px;top:2483px;list-style:none;font-size:14px;font-weight:500;color:#2d3b46}
.best-list li{display:flex;align-items:center;gap:10px;height:28px}
.best-mark{left:604px;top:2320px;width:384px;height:384px;border-radius:50%;background:var(--green-soft);display:flex;align-items:center;justify-content:center;font-size:64px;font-weight:600;color:var(--green)}

/* clients */
.client{position:absolute;top:2904px;width:160px;height:160px;border-radius:50%;background:var(--white);box-shadow:0 8px 28px rgba(0,0,0,.09);display:flex;align-items:center;justify-content:center;text-align:center;font-size:15px;font-weight:600;color:var(--navy);line-height:1.2}

/* testimonial */
.testi-title{left:0;top:3150px;width:1200px;text-align:center;font-size:41px;font-weight:600;line-height:49px;color:var(--navy)}
.avatar{left:532px;top:3301px;width:136px;height:136px;border-radius:50%;background:linear-gradient(180deg,#dfe6ec 0%,#b9c6d1 100%)}
.testi-name{left:0;top:3449px;width:1200px;text-align:center;font-size:11.5px;font-weight:500}
.stars{left:0;top:3470px;width:1200px;text-align:center;color:#f3a53a;font-size:13px;letter-spacing:1px}
.testi-quote{left:262px;top:3497px;width:676px;text-align:center;font-size:13.5px;line-height:23px;color:var(--text)}
.dot{position:absolute;left:1095px;width:14px;height:14px;border-radius:50%;background:#c9ccd0}

/* contact band */
.footer-bg{left:0;top:3850px}
.cta{left:138px;top:3747px;width:924px;height:203px;border-radius:102px;background:var(--green)}
.cta-title{left:219px;top:3800px;font-size:42px;font-weight:600;color:var(--white)}
.cta-text{left:219px;top:3858px;width:420px;font-size:13px;line-height:19px;color:var(--white)}
.cta-btn{left:843px;top:3831px;width:140px;height:42px;background:var(--white);color:var(--navy);font-size:12px}

/* footer */
.foot-brand{left:96px;top:4207px;display:flex;align-items:center;gap:12px;color:var(--white)}
.foot-brand .brand-dot{background:var(--white);width:66px;height:66px}
.foot-brand .brand-name{color:var(--white);font-size:36px}
.foot-brand .brand-tag{color:#c8d1d8}
.foot-col{position:absolute;color:var(--white)}
.foot-col h5{font-size:19px;font-weight:500;margin-bottom:18px}
.foot-col ul{list-style:none;font-size:12.5px}
.foot-col li{height:31px;display:flex;align-items:flex-start;gap:8px}
.news p{font-size:12.5px;line-height:18px;width:240px}
.news-input{margin-top:12px;width:259px;height:42px;border-radius:22px;background:#1c394b;display:flex;align-items:center;justify-content:space-between;padding:0 18px;font-size:12px;color:#aab7c1}
.foot-rule{left:89px;top:4445px;width:1024px;border-top:1px solid #2a4557}
.copyright{left:0;top:4466px;width:1200px;text-align:center;font-size:12px;font-weight:500;color:var(--white)}
.social{left:1129px;top:4426px;width:40px;height:40px;border-radius:50%;background:var(--green)}
</style>
</head>
<body>

<!-- header -->
<div class="abs topbar">
  <span><svg width="13" height="10" viewBox="0 0 13 10"><rect x=".5" y=".5" width="12" height="9" rx="1" fill="none" stroke="#fff"/><path d="M1 1l5.5 4.5L12 1" fill="none" stroke="#fff"/></svg>Email Us</span>
  <span><svg width="12" height="12" viewBox="0 0 24 24"><path fill="#fff" d="M6.6 10.8a15 15 0 006.6 6.6l2.2-2.2a1 1 0 011-.25 11.4 11.4 0 003.6.6 1 1 0 011 1V20a1 1 0 01-1 1A17 17 0 013 4a1 1 0 011-1h3.5a1 1 0 011 1 11.4 11.4 0 00.6 3.6 1 1 0 01-.25 1z"/></svg>Call Us: +61 (08) 5550 1234</span>
</div>
<div class="abs brand">
  <div class="brand-dot"></div>
  <div><div class="brand-name">Velmora</div><div class="brand-tag">odours controlled naturally</div></div>
</div>
<nav class="abs nav">
  <a>Odour Control Products</a><a>How Biofiltration Works</a><a>Odour Control by Industry</a><a>Past Projects</a><a>About Us</a><a>Contact</a>
</nav>

<!-- hero -->
<div class="photo hero-photo-big" role="img" aria-label="Man with outstretched arms on a green mountain plateau under a blue sky"></div>
<div class="photo hero-photo-small" role="img" aria-label="Woman raising her arms joyfully in a green forest"></div>
<h1 class="abs hero-title">We Are<br>Odours Controlled<br>Naturally</h1>
<p class="abs hero-sub">Velmora uses sustainable biotechnology to resolve odour..</p>
<a class="btn" style="left:89px;top:483px;width:176px;height:42px">REQUEST A QUOTE</a>

<!-- odours control -->
<h2 class="h2" style="top:762px">Odours Control</h2>
<div class="feature" style="left:227px">
  <svg width="80" height="80" viewBox="0 0 80 80" fill="none" stroke="#6cb33f" stroke-width="2.4" stroke-linejoin="round"><path d="M14 38l26-10 26 10-26 10z"/><path d="M14 38v24l26 10 26-10V38"/><path d="M40 48v24"/><path d="M14 38l-8 10 26 10 8-10M66 38l8 10-26 10-8-10"/><circle cx="40" cy="20" r="10"/><path d="M35 20l4 4 7-7"/><path d="M40 3v3M26 8l2 3M54 8l-2 3M22 20h3M55 20h3"/></svg>
  <h3>Products</h3>
  <p>Aenean sollicitudin lorem quis bibendum auctor nisi elit consequat.</p>
  <hr>
</div>
<div class="feature" style="left:481px">
  <svg width="80" height="80" viewBox="0 0 80 80" fill="none" stroke="#6cb33f" stroke-width="2.4" stroke-linejoin="round"><rect x="6" y="8" width="30" height="22" rx="2"/><path d="M12 24v-4M18 24v-8M24 24v-6M30 24v-10"/><rect x="6" y="36" width="22" height="16" rx="2"/><path d="M10 44h14"/><rect x="34" y="48" width="40" height="26"/><path d="M34 58h40M48 48v10h12V48"/><path d="M46 10l10 10 14-14M60 30v14"/><circle cx="62" cy="30" r="5"/><path d="M4 74h72"/></svg>
  <h3>Features</h3>
  <p>Aenean sollicitudin lorem quis bibendum auctor nisi elit consequat.</p>
  <hr><div class="more">READ MORE</div>
</div>
<div class="feature" style="left:731px">
  <svg width="80" height="80" viewBox="0 0 80 80" fill="none" stroke="#6cb33f" stroke-width="2.4" stroke-linejoin="round"><rect x="14" y="8" width="44" height="66" rx="3"/><rect x="26" y="4" width="20" height="8" rx="2"/><path d="M22 26h6M34 26h16M22 40h6M34 40h16M22 54h6M34 54h12"/><path d="M46 60l22-22 5 5-22 22-7 2z"/></svg>
  <h3>Past Projects</h3>
  <p>Aenean sollicitudin lorem quis bibendum auctor nisi elit consequat.</p>
  <hr><div class="more">READ MORE</div>
</div>

<!-- about -->
<svg class="abs about-bg" width="1200" height="560" viewBox="0 0 1200 560" role="img" aria-label="Green grass field background">
  <defs><linearGradient id="grass" x1="0" y1="0" x2="0" y2="1"><stop offset="0" stop-color="#7dbf45"/><stop offset="1" stop-color="#5ea832"/></linearGradient></defs>
  <path d="M0,145 C60,55 160,30 260,55 C340,80 370,190 450,215 C640,265 920,205 1200,20 L1200,560 L0,560 Z" fill="url(#grass)"/>
</svg>
<div class="photo about-photo" role="img" aria-label="Two people walking bicycles along a sunlit country path"></div>
<h2 class="abs about-title">About Velmora</h2>
<h3 class="abs about-sub">Odour Control Solutions About Velmora</h3>
<p class="abs about-text">Velmora uses sustainable biotechnology to resolve odour and corrosion problems in a highly efficient, environmentally friendly and cost-effective manner. Our, products, the VelVent series of biofilters have been specifically engineered to overcome issues traditionally associated with biofiltration, such as bed compaction and uneven moisture levels, and our patented design achieves a removal rate of up to 99.9% per stage of treatment.</p>
<a class="btn" style="left:660px;top:1586px;width:177px;height:42px">REQUEST A QUOTE</a>

<!-- projects -->
<div class="project" style="left:89px">
  <div class="pic" role="img" aria-label="Green biofilter tanks at a pump station"></div>
  <h4>Kestrel SPS</h4>
  <p>3000 m3/h- H2S 400ppm- Kestrel SPS: Odour treatment for balance tanks &amp; wastewater...</p>
  <div class="more">READ MORE</div>
</div>
<div class="project" style="left:348px">
  <div class="pic" role="img" aria-label="Green biofilter tanks in front of a brick building"></div>
  <h4>Maple Street Pump Station</h4>
  <p>3000 m3/h- H2S 250ppm- Maple Street Pump Station: preventing odours and corrosion...</p>
  <div class="more">READ MORE</div>
</div>
<div class="project" style="left:607px">
  <div class="pic" role="img" aria-label="Row of biofilter tanks at a wastewater plant under blue sky"></div>
  <h4>Ashford City</h4>
  <p>2800 m3/h- H2S 300ppm- Ashford City Council Wastewater Reclamation Plant Odour...</p>
  <div class="more">READ MORE</div>
</div>
<div class="project" style="left:866px">
  <div class="pic" role="img" aria-label="Biofilter tanks behind a black security fence"></div>
  <h4>Denton Street WWPS</h4>
  <p>3000 m3/h- H2S 300ppm- Denton Street WWPS Odour Treatment Plant</p>
  <div class="more">READ MORE</div>
</div>

<!-- what makes us best -->
<h2 class="abs best-title">What makes us<br>the best?</h2>
<ul class="abs best-list">
  <li><svg width="14" height="14" viewBox="0 0 14 14"><circle cx="7" cy="7" r="7" fill="#6cb33f"/><path d="M4 7.2l2 2 4-4" stroke="#fff" stroke-width="1.6" fill="none"/></svg>Biological &amp; Sustainable technology</li>
  <li><svg width="14" height="14" viewBox="0 0 14 14"><circle cx="7" cy="7" r="7" fill="#6cb33f"/><path d="M4 7.2l2 2 4-4" stroke="#fff" stroke-width="1.6" fill="none"/></svg>Efficient maintenance cost</li>
  <li><svg width="14" height="14" viewBox="0 0 14 14"><circle cx="7" cy="7" r="7" fill="#6cb33f"/><path d="M4 7.2l2 2 4-4" stroke="#fff" stroke-width="1.6" fill="none"/></svg>100% Australian Owned</li>
  <li><svg width="14" height="14" viewBox="0 0 14 14"><circle cx="7" cy="7" r="7" fill="#6cb33f"/><path d="M4 7.2l2 2 4-4" stroke="#fff" stroke-width="1.6" fill="none"/></svg>Eco Friendly</li>
</ul>
<a class="btn" style="left:212px;top:2612px;width:176px;height:42px">REQUEST A QUOTE</a>
<div class="abs best-mark">Velmora</div>

<!-- clients -->
<h2 class="h2" style="top:2818px">Our Happy Clients</h2>
<div class="client" style="left:165px">Harbour<br>City</div>
<div class="client" style="left:342px">Sandmere<br>Coast</div>
<div class="client" style="left:520px">Redland<br>Territory</div>
<div class="client" style="left:698px">Clearflow<br>Water</div>
<div class="client" style="left:877px">Ridgeway<br>Water</div>

<!-- testimonial -->
<h2 class="abs testi-title">As soon as the system was started, the<br>smell disappeared!</h2>
<div class="photo avatar" role="img" aria-label="Portrait of the client"></div>
<div class="abs testi-name">Liam Carter</div>
<div class="abs stars">★★★★★</div>
<p class="abs testi-quote">“Marcus and the Velmora team promised to stop the odour from our smelly neighbor and they delivered- in spades! As soon as the system was started, the smell disappeared. The system is well designed, very professionally installed and the beauty of it is, apart from a constantly running fan, it is bacteria doing the heavy lifting, so it is very environmentally friendly. We lived with the smell for 3 three years which could be extremely frustrating and unpleasant. Now, the problem is solved and we can have BBQs again. We are happy and our neighbours have noticed the odour is gone. Thank you!”</p>
<span class="dot" style="top:3436px"></span>
<span class="dot" style="top:3458px"></span>
<span class="dot" style="top:3480px;background:var(--green)"></span>

<!-- footer background + contact band -->
<svg class="abs footer-bg" width="1200" height="655" viewBox="0 0 1200 655">
  <path d="M640,110 C850,105 1050,70 1200,20 L1200,60 C1050,105 850,125 640,115 Z" fill="#cfe6bd"/>
  <path d="M0,20 C260,100 620,125 1200,45 L1200,655 L0,655 Z" fill="#0e2a3b"/>
</svg>
<div class="abs cta"></div>
<h2 class="abs cta-title">Get in Contact</h2>
<p class="abs cta-text">If you have any queries regarding out products, please do not hesitate to contact us</p>
<a class="btn cta-btn">CONTACT US</a>

<!-- footer -->
<div class="abs foot-brand">
  <div class="brand-dot"></div>
  <div><div class="brand-name">Velmora</div><div class="brand-tag">odours controlled naturally</div></div>
</div>
<div class="foot-col" style="left:381px;top:4132px">
  <h5>Quick links</h5>
  <ul>
    <li>› Odour Control Products</li><li>› How Biofiltration Works</li><li>› Odour Control by Industry</li><li>› Past Projects</li><li>› About Us</li><li>› Contact</li>
  </ul>
</div>
<div class="foot-col" style="left:600px;top:4132px">
  <h5>Contact info</h5>
  <ul>
    <li><svg width="13" height="13" viewBox="0 0 24 24"><path fill="#6cb33f" d="M6.6 10.8a15 15 0 006.6 6.6l2.2-2.2a1 1 0 011-.25 11.4 11.4 0 003.6.6 1 1 0 011 1V20a1 1 0 01-1 1A17 17 0 013 4a1 1 0 011-1h3.5a1 1 0 011 1 11.4 11.4 0 00.6 3.6 1 1 0 01-.25 1z"/></svg>+61 (08) 5550 1234</li>
    <li><svg width="13" height="11" viewBox="0 0 13 10"><rect x="0" y="0" width="13" height="10" rx="1" fill="#6cb33f"/><path d="M1 1l5.5 4.5L12 1" fill="none" stroke="#0e2a3b"/></svg>Email Us</li>
    <li style="height:auto;line-height:20px"><svg width="12" height="15" viewBox="0 0 12 16" style="margin-top:2px"><path fill="#6cb33f" d="M6 0a6 6 0 00-6 6c0 4.5 6 10 6 10s6-5.5 6-10a6 6 0 00-6-6zm0 8.5A2.5 2.5 0 116 3.5a2.5 2.5 0 010 5z"/></svg><span>12 Sample Lane, Greenvale<br>WA 6000, Australia</span></li>
  </ul>
</div>
<div class="foot-col news" style="left:850px;top:4134px">
  <h5>Newsletter</h5>
  <p>Subscribe to our email address to get the latest news.</p>
  <div class="news-input"><span>✉&nbsp; Enter Your Email...</span><svg width="16" height="16" viewBox="0 0 16 16"><path d="M1 7.5L15 1 10 15 7.5 9z" fill="#6cb33f"/></svg></div>
</div>
<div class="abs foot-rule"></div>
<div class="abs social"></div>
<p class="abs copyright">© Copyright Velmora 2023 All Rights Reserved</p>

</body>
</html>
```